TotPlanet Community Landing Page

TotPlanet is a virtual world built with childrens' needs in mind. It is an online portal where parents will find all kids' related stuffs and a community connect point for parents to interact and share their experiences.

We need the designs for 2 pages within TotPlanet:
- Landing Page for the Community Area
- Registration page for membership

1) The Landing Page need to have the following:

Logo & Main Background :- use the images attached

Page Title & Navigation Menu :-
The page title is "Community Connect"; navigation menu should be able to hold at least 6 tabs

Login Widget* :-
We want to put emphasis on the design of this.
For visitors, this is a normal login widget with username/password input fields, register button and 'login with chatterbook' button.
For logged-in users, this becomes a simple dashboard widget with Avatar, shortlinks and some useful navigation buttons.

"Groups" Section :-
This area holds an image, a short paragraph introducing "Groups", a widget showing 5-10 latest/popular groups and a 'Go to Groups' button at the bottom.

"Forum" Section :-
This area holds an image, a short paragraph introducing "Forum", a widget showing 5-10 latest/popular discussion topics and a 'Go to Forum' button at the bottom.

"Activities" Section -
This area holds an image, a short paragraph introducing "Forum", a widget showing 5-10 latest/popular events & activities and a 'Go to Activities' button at the bottom.

"Marketplace" Section :-
This area holds an image, a short paragraph introducing "Marketplace", a widget showing 5-10 latest/popular products and a 'Go to Marketplace' button at the bottom.

Social Media elements :-
The usual social media icons and chatterbook like box.

2) The Registration Page will need to contain the registration form as per the image attached.

Target Market(s)

Parents with kids ranging from 2 - 12 years old

Industry/Entity Type

Events

Requirements
Nice to have
• - colorful illustrations of kids or kids related images all around

```html
<!DOCTYPE html>
<html lang="en">
<head>
<meta charset="utf-8">
<title>TotPlanet – Community Connect</title>
<link href="https://fonts.googleapis.com/css2?family=Open+Sans:wght@400;600;700&family=PT+Sans:wght@400;700&family=Fredoka:wght@600&display=swap" rel="stylesheet">
<style>
:root{
  --sky-top:#3fb4e4;
  --sky-low:#a9dcf3;
  --grass:#5e9a22;
  --grass-dark:#3f7417;
  --panel:#ffffff;
  --text:#555555;
  --title:#222222;
  --bullet:#2c6db5;
  --groups:#f7941d;
  --groups-head:#f08a1c;
  --forum:#5b3fae;
  --forum-head:#2f5fa8;
  --activities:#a51212;
  --activities-head:#c3141b;
  --market:#3e8a26;
  --market-head:#3a7d1e;
  --login-red:#d9141b;
  --cb-blue:#3b5b9a;
  --chirp:#1fb8dd;
  --dark:#2a2a2a;
}
*{box-sizing:border-box;margin:0;padding:0}
html,body{width:1200px;height:2214px;overflow:hidden}
body{position:relative;font-family:"Open Sans",sans-serif;color:var(--text);background:var(--grass)}
.scenery{position:absolute;inset:0;background:linear-gradient(180deg,var(--sky-top) 0,var(--sky-low) 380px,#dff1f9 470px,#8fc43a 520px,var(--grass) 640px,var(--grass-dark) 1400px,var(--grass) 2214px)}
.abs{position:absolute}

/* header */
.brand{left:160px;top:30px;width:280px;height:120px;display:flex;align-items:center;gap:14px}
.brand-dot{width:46px;height:46px;border-radius:50%;background:#e8342f}
.brand-name{font-family:"Fredoka",sans-serif;font-weight:600;font-size:50px;color:#ffffff;white-space:nowrap}
.login{left:657px;top:0;width:359px;height:82px;background:rgba(255,255,255,.55);border:1px solid rgba(255,255,255,.8);border-top:0;border-radius:0 0 6px 6px}
.login-field{position:absolute;top:13px;width:158px;height:26px;background:#fff;border:1px solid #c8c8c8;border-radius:5px;font-size:11px;color:#666;padding:5px 0 0 34px;white-space:nowrap}
.login-field.user{left:15px}
.login-field.pass{left:189px}
.login-btn{position:absolute;right:12px;top:48px;width:66px;height:22px;background:var(--login-red);color:#fff;font-size:12px;text-align:center;line-height:20px;border-radius:3px;border:1px solid #fff}
.cb-login{left:676px;top:103px;width:182px;height:30px;background:linear-gradient(#6f8ec9,var(--cb-blue));border-radius:3px;color:#fff;font-size:11.5px;line-height:30px;padding-left:34px;white-space:nowrap;overflow:hidden}
.cb-login::before{content:"";position:absolute;left:9px;top:7px;width:16px;height:16px;background:#fff;opacity:.85;border-radius:2px}

.nav{left:134px;top:173px;width:929px;height:43px;background:linear-gradient(#fff,#e8e8e8);border-radius:4px;display:flex;box-shadow:0 2px 3px rgba(0,0,0,.2)}
.nav a{display:block;height:43px;line-height:43px;padding:0 28px;font-size:14px;color:#444;text-decoration:none;border-right:1px solid #d3d3d3;letter-spacing:.3px;white-space:nowrap}
.nav a:nth-child(1){padding:0 26px 0 44px}
.nav a:last-child{border-right:0}

.slider{left:134px;top:242px;width:929px;height:360px;background:rgba(255,255,255,.35);border-radius:8px}
.slide{left:143px;top:251px;width:911px;height:342px;border-radius:6px;background:linear-gradient(180deg,#2e86d1 0,#6fb6ec 55%,#cfe7f7 100%)}
.slide-caption{left:765px;top:376px;width:280px;color:#fff}
.slide-caption h2{font-family:"PT Sans",sans-serif;font-size:25px;font-weight:700;text-shadow:0 2px 3px rgba(0,0,0,.5);white-space:nowrap}
.slide-caption p{font-size:11px;line-height:20px;margin-top:10px}
.pager{left:520px;top:566px;width:160px;height:32px;background:linear-gradient(#6a6a6a,#2c2c2c);border-radius:10px 10px 0 0;display:flex;justify-content:center;align-items:center;gap:12px}
.pager span{width:12px;height:12px;border-radius:50%;background:#111}
.pager span.on{background:#f7a21d}

/* content panel */
.panel{left:134px;top:632px;width:929px;height:1103px;background:var(--panel);border-radius:6px;box-shadow:0 0 6px rgba(0,0,0,.25)}
.section{position:absolute;width:425px;height:484px}
.sec-head{display:flex;align-items:center;height:50px;gap:14px;padding-left:2px}
.sec-icon{width:58px;height:46px;border-radius:10px}
.sec-head h3{font-family:"PT Sans",sans-serif;font-weight:400;font-size:25px;color:var(--head)}
.intro{position:absolute;top:56px;left:4px;right:0;height:106px}
.intro-photo{position:absolute;left:0;top:0;width:195px;height:106px;border:2px solid #ddd;border-radius:4px}
.intro-text{position:absolute;left:204px;top:0;right:0;font-size:10.5px;line-height:16px;text-align:justify}
.intro-text strong{display:block;font-size:12.5px;color:var(--title);font-weight:600;margin-bottom:3px;text-align:left;white-space:nowrap}
.list-box{position:absolute;left:0;top:186px;width:425px;height:298px;background:#fff;border:1px solid #ddd;border-radius:4px;box-shadow:0 1px 4px rgba(0,0,0,.12)}
.list-box ul{list-style:none;padding:18px 20px 0 26px}
.list-box li{position:relative;font-size:10.5px;line-height:16px;padding-left:20px;height:46px;color:#444}
.list-box li::before{content:"";position:absolute;left:0;top:4px;width:9px;height:9px;background:var(--bullet);border-radius:1px}
.list-box li::after{content:"";position:absolute;left:3px;top:6px;border-left:4px solid #fff;border-top:2.5px solid transparent;border-bottom:2.5px solid transparent}
.go{position:absolute;left:0;right:0;bottom:0;height:42px;background:var(--accent);color:#fff;font-size:15px;text-align:right;line-height:42px;padding-right:20px;border-radius:0 0 4px 4px;white-space:nowrap}
.go::before{content:"→ "}
.s-groups{left:158px;top:668px;--accent:var(--groups);--head:var(--groups-head)}
.s-forum{left:620px;top:668px;--accent:var(--forum);--head:var(--forum-head)}
.s-activities{left:158px;top:1220px;--accent:var(--activities);--head:var(--activities-head)}
.s-market{left:620px;top:1220px;--accent:var(--market);--head:var(--market-head)}

/* footer widgets */
.feed-cb{left:140px;top:1768px;width:298px;height:287px;background:#fff;border:5px solid #2f63b0;border-radius:6px}
.feed-cb h4{height:38px;margin:4px;background:#fff;border:1px solid #9cb3d8;border-radius:6px;font-family:"PT Sans",sans-serif;font-size:17px;color:#2f4f8c;line-height:36px;padding-left:58px;position:relative;white-space:nowrap}
.feed-cb h4::before{content:"";position:absolute;left:8px;top:-6px;width:40px;height:40px;border-radius:50%;background:#2f63b0}
.cb-item{display:flex;gap:8px;padding:6px 12px;font-size:10px;line-height:13px;color:#777}
.cb-item .av{width:34px;height:34px;flex:none;background:#d8a07a}
.cb-item b{display:block;font-weight:400;font-size:12.5px;color:#2f63b0;line-height:16px}
.cb-likes{font-size:9px;padding:6px 12px;color:#333}
.cb-likes span{color:#2f63b0}
.cb-faces{display:grid;grid-template-columns:repeat(6,38px);gap:4px 6px;padding:4px 12px}
.cb-faces i{display:block;height:38px;background:#c9c1b8}

.feed-ch{left:481px;top:1768px;width:298px;height:287px;background:#fff;border:2px solid #d7d7d7;border-radius:6px;padding:8px 10px}
.feed-ch h4{height:36px;background:var(--chirp);border-radius:4px;color:#fff;font-family:"PT Sans",sans-serif;font-size:15px;line-height:36px;padding-left:76px;position:relative}
.feed-ch h4::before{content:"";position:absolute;left:18px;top:-4px;width:40px;height:40px;border-radius:50%;background:#7fd4ea}
.ch-item{font-size:10px;line-height:16px;color:#888;padding:10px 0 0 14px;position:relative}
.ch-item::before{content:"›";position:absolute;left:2px;top:8px;color:var(--chirp);font-size:15px}
.ch-item a{color:#2a8ed0;text-decoration:none;display:block;word-break:break-all}
.ch-item em{font-style:normal;color:#2a8ed0;padding-left:4px}
.view{position:absolute;left:160px;bottom:12px;width:116px;height:32px;background:var(--chirp);color:#fff;border-radius:4px;text-align:center;line-height:32px;font-size:11px}

.social{left:822px;top:1768px;width:248px;height:287px;background:var(--dark);border-radius:6px}
.social a{position:absolute;left:38px;width:172px;height:30px;border-radius:3px;color:#fff;font-size:12px;line-height:30px;padding-left:33px;text-decoration:none;white-space:nowrap;overflow:hidden}
.social a::before{content:"";position:absolute;left:9px;top:7px;width:16px;height:16px;border-radius:3px;background:rgba(255,255,255,.8)}
.sb-chirp{top:36px;background:linear-gradient(#8fcdf1,#4ba8de)}
.sb-cb{top:97px;background:linear-gradient(#6f8ec9,var(--cb-blue))}
.sb-rss{top:159px;background:linear-gradient(#ffb049,#f27b0c)}
.sb-globe{top:219px;background:linear-gradient(#444,#111)}

.foot-links{left:0;width:1200px;top:2142px;text-align:center;font-size:11px;color:#fff}
.foot-links span{padding:0 8px}
.copy{left:0;width:1200px;top:2167px;text-align:center;font-size:11px;color:#fff}
</style>
</head>
<body>
<div class="scenery" role="img" aria-label="Cartoon sky with rainbow and clouds over green rolling hills with butterflies"></div>

<header>
  <div class="abs brand"><span class="brand-dot"></span><span class="brand-name">TotPlanet</span></div>
  <form class="abs login">
    <div class="login-field user">User Name</div>
    <div class="login-field pass">Password</div>
    <div class="login-btn">LOGIN</div>
  </form>
  <div class="abs cb-login">Log in with Chatterbook</div>
  <nav class="abs nav">
    <a href="#">HOME</a><a href="#">GROUPS</a><a href="#">FORUMS</a><a href="#">ACTIVITIES</a><a href="#">MARKETPLACE</a><a href="#">CONTACT US</a>
  </nav>
</header>

<div class="abs slider"></div>
<div class="abs slide" role="img" aria-label="Photo of five happy children jumping against a blue sky"></div>
<div class="abs slide-caption">
  <h2>LOREUM IPSUM DOLLAR</h2>
  <p>Cum sociis natoque penatibus et magnis dis parturient montes, nascetur ridiculus mus. In iaculis facilisis massa. Etiam eu urna. Sed porta.Cum sociis natoque penatibus et magnis</p>
</div>
<div class="abs pager"><span class="on"></span><span></span><span></span><span></span></div>

<main>
<div class="abs panel"></div>

<section class="section s-groups">
  <div class="sec-head"><span class="sec-icon" role="img" aria-label="Illustration of a group of cartoon kids" style="background:#f3b35c"></span><h3>GROUPS</h3></div>
  <div class="intro">
    <div class="intro-photo" role="img" aria-label="Photo of smiling children in a circle" style="background:linear-gradient(135deg,#c9866a,#e6b38f)"></div>
    <p class="intro-text"><strong>Mauris Lacus Vestibulum Volutpat.</strong>Sed ut perspiciatis unde omnis iste natus error sit voluptatem accusantium doloremque laudantium, totam rem aperiam, eaque ipsa quae ab illo inventore veritatis et quasi</p>
  </div>
  <div class="list-box"><ul>
    <li>Sed ut perspiciatis unde omnis iste natus error sit voluptatem accusan-tium doloremque laudantium, totam rem aperiam, eaque ipsa quae .</li>
    <li>Sed ut perspiciatis unde omnis iste natus error sit voluptatem accusan-tium doloremque laudantium, totam rem aperiam, eaque ipsa quae .</li>
    <li>Sed ut perspiciatis unde omnis iste natus error sit voluptatem accusan-tium doloremque laudantium, totam rem aperiam, eaque ipsa quae .</li>
    <li>Sed ut perspiciatis unde omnis iste natus error sit voluptatem accusan-tium doloremque laudantium, totam rem aperiam, eaque ipsa quae .</li>
    <li>Sed ut perspiciatis unde omnis iste natus error sit voluptatem accusan-tium doloremque laudantium, totam rem aperiam, eaque ipsa quae .</li>
  </ul><div class="go">Go to Groups</div></div>
</section>

<section class="section s-forum">
  <div class="sec-head"><span class="sec-icon" role="img" aria-label="Illustration of chat bubbles and people" style="background:#6fa0d8"></span><h3>FORUM</h3></div>
  <div class="intro">
    <div class="intro-photo" role="img" aria-label="Photo of a little girl blowing bubbles in a park" style="background:linear-gradient(135deg,#6f9a3c,#b9d48a)"></div>
    <p class="intro-text"><strong>Mauris Lacus Vestibulum Volutpat.</strong>Sed ut perspiciatis unde omnis iste natus error sit voluptatem accusantium doloremque laudantium, totam rem aperiam, eaque ipsa quae ab illo inventore veritatis et quasi</p>
  </div>
  <div class="list-box"><ul>
    <li>Sed ut perspiciatis unde omnis iste natus error sit voluptatem accusan-tium doloremque laudantium, totam rem aperiam, eaque ipsa quae .</li>
    <li>Sed ut perspiciatis unde omnis iste natus error sit voluptatem accusan-tium doloremque laudantium, totam rem aperiam, eaque ipsa quae .</li>
    <li>Sed ut perspiciatis unde omnis iste natus error sit voluptatem accusan-tium doloremque laudantium, totam rem aperiam, eaque ipsa quae .</li>
    <li>Sed ut perspiciatis unde omnis iste natus error sit voluptatem accusan-tium doloremque laudantium, totam rem aperiam, eaque ipsa quae .</li>
    <li>Sed ut perspiciatis unde omnis iste natus error sit voluptatem accusan-tium doloremque laudantium, totam rem aperiam, eaque ipsa quae .</li>
  </ul><div class="go">Go to Forum</div></div>
</section>

<section class="section s-activities">
  <div class="sec-head"><span class="sec-icon" role="img" aria-label="Illustration of a child on a sled" style="background:#d9e2ee"></span><h3>ACTIVITIES</h3></div>
  <div class="intro">
    <div class="intro-photo" role="img" aria-label="Photo of children looking into a glass jar" style="background:linear-gradient(135deg,#5e5347,#c9a27c)"></div>
    <p class="intro-text"><strong>Mauris Lacus Vestibulum Volutpat.</strong>Sed ut perspiciatis unde omnis iste natus error sit voluptatem accusantium doloremque laudantium, totam rem aperiam, eaque ipsa quae ab illo inventore veritatis et quasi</p>
  </div>
  <div class="list-box"><ul>
    <li>Sed ut perspiciatis unde omnis iste natus error sit voluptatem accusan-tium doloremque laudantium, totam rem aperiam, eaque ipsa quae .</li>
    <li>Sed ut perspiciatis unde omnis iste natus error sit voluptatem accusan-tium doloremque laudantium, totam rem aperiam, eaque ipsa quae .</li>
    <li>Sed ut perspiciatis unde omnis iste natus error sit voluptatem accusan-tium doloremque laudantium, totam rem aperiam, eaque ipsa quae .</li>
    <li>Sed ut perspiciatis unde omnis iste natus error sit voluptatem accusan-tium doloremque laudantium, totam rem aperiam, eaque ipsa quae .</li>
    <li>Sed ut perspiciatis unde omnis iste natus error sit voluptatem accusan-tium doloremque laudantium, totam rem aperiam, eaque ipsa quae .</li>
  </ul><div class="go">Go to Activities</div></div>
</section>

<section class="section s-market">
  <div class="sec-head"><span class="sec-icon" role="img" aria-label="Illustration of a shopping basket" style="background:#8fc5dc"></span><h3>MARKETPLACE</h3></div>
  <div class="intro">
    <div class="intro-photo" role="img" aria-label="Photo of a baby with a plush toy" style="background:linear-gradient(135deg,#e1b9a0,#9a5a32)"></div>
    <p class="intro-text"><strong>Mauris Lacus Vestibulum Volutpat.</strong>Sed ut perspiciatis unde omnis iste natus error sit voluptatem accusantium doloremque laudantium, totam rem aperiam, eaque ipsa quae ab illo inventore veritatis et quasi</p>
  </div>
  <div class="list-box"><ul>
    <li>Sed ut perspiciatis unde omnis iste natus error sit voluptatem accusan-tium doloremque laudantium, totam rem aperiam, eaque ipsa quae .</li>
    <li>Sed ut perspiciatis unde omnis iste natus error sit voluptatem accusan-tium doloremque laudantium, totam rem aperiam, eaque ipsa quae .</li>
    <li>Sed ut perspiciatis unde omnis iste natus error sit voluptatem accusan-tium doloremque laudantium, totam rem aperiam, eaque ipsa quae .</li>
    <li>Sed ut perspiciatis unde omnis iste natus error sit voluptatem accusan-tium doloremque laudantium, totam rem aperiam, eaque ipsa quae .</li>
    <li>Sed ut perspiciatis unde omnis iste natus error sit voluptatem accusan-tium doloremque laudantium, totam rem aperiam, eaque ipsa quae .</li>
  </ul><div class="go">Go to Marketplace</div></div>
</section>
</main>

<footer>
  <aside class="abs feed-cb">
    <h4>Chatterbook Feeds</h4>
    <div class="cb-item"><span class="av" role="img" aria-label="Member avatar photo"></span><div><b>Sed ut perspiciatis unde</b>voluptatem accusantium doloremque laudantium, totam rem aperiam,</div></div>
    <div class="cb-item"><span class="av" role="img" aria-label="Member avatar photo"></span><div><b>Sed ut perspiciatis unde</b>voluptatem accusantium doloremque laudantium, totam rem aperiam,</div></div>
    <p class="cb-likes">You and 14,596 others like <span>Dana Reed.</span></p>
    <div class="cb-faces" role="img" aria-label="Grid of member profile photos">
      <i></i><i></i><i></i><i></i><i></i><i></i><i></i><i></i><i></i><i></i>
    </div>
  </aside>

  <aside class="abs feed-ch">
    <h4>Chirper Feeds</h4>
    <p class="ch-item">Sed ut perspiciatis unde omnis iste natus error sit voluptatem accusantium doloremque laudantium <a href="#">https://www.searchly.co/search?hl=en&amp;q=young%20people%20within%20our%20Comm</a><em>Like :: Chirp :: Favourite</em></p>
    <p class="ch-item">Sed ut perspiciatis unde omnis iste natus error sit voluptatem accusantium doloremque laudantium <a href="#">https://www.searchly.co/search?hl=en&amp;q=young%20people%20within%20our%20Comm</a><em>Like :: Chirp :: Favourite</em></p>
    <div class="view">VIEW &gt;&gt;</div>
  </aside>

  <aside class="abs social">
    <a class="sb-chirp" href="#">On Chirper</a>
    <a class="sb-cb" href="#">Share On Chatterbook</a>
    <a class="sb-rss" href="#">Rss Feed</a>
    <a class="sb-globe" href="#">on Globe +</a>
  </aside>

  <p class="abs foot-links"><span>Terms &amp; Condtions</span>|<span>Privacy Statement</span>|<span>Contact Us</span></p>
  <p class="abs copy">© 2013 totplanet., All rights reserved</p>
</footer>
</body>
</html>
```